Tova Meadows brand , chocolate packaging design

Tova Meadows

Products List

CANNABIS INFUSED CHOCOLATE BAR
(4 Flavor Chocolate Bar)
Original Milk chocolate Bar
Cookies N Cream Bar
Strawberry Cheesecake Bar
S’mores Bar

Information Front
-1000 MG THC Per package
-100mg THC per serving
-Made with Belgian Chocolate
-Made with Quality California Cannabis Extracts
-Net weight of bar 50grams
-California triangle warning symbol
-Flavor of chocolate bar

Information Back

-10 Servings per package
-100 mg serving size

-Directions
Wait 1-2 hours for full effect before consuming more.
-Very potent , Keep out of reach of children

-Store at 68-77° F
-Will melt in prolonged heat
-California government warning and ad41notice website

Ingredient list

Milk chocolate Bar
MILK CHOCOLATE (SUGAR, COCOA BUTTER , UNSWEETENED CHOCOLATE, SUNFLOWER LECITHIN, VANILLA) , CANNABIS EXTRACT.
ALLERGENS-CONTAINS MILK

Strawberry Cheesecake
WHITE CHOCOLATE (SUGAR, COCOA BUTTER, WHOLE MILK POWDER ,SOY LECITHIN, NATURAL VANILLA FLAVOR) STRAWBERRY POWDER , STRAWBERRY EXTRACT , NATURAL FLAVORS, CANNABIS EXTRACT.

Cookies n cream
WHITE CHOCOLATE (SUGAR, COCOA BUTTER, WHOLE MILK POWDER ,SOY LECITHIN, NATURAL VANILLA FLAVOR) 9
KRUNDELS (SUGAR, WHITE RICE FLOUR, TAPIOCA STARCH, PALM OIL, CANOLA OIL, WHOLE OAT FLOUR, CORN STARCH , COCOA (PROCESSED WITH ALKALI), INVERT SUGAR, SOY LECITHIN, BAKING SODA, SALT, XANTHAM GUM , CHOCOLATE, ARTIFICIAL FLAVOR, CANNABIS EXTRACT

S’mores
MILK CHOCOLATE (SUGAR, COCOA BUTTER, MILK, UNSWEETENED CHOCOLATE ,SUNFLOWER LECITHIN, VANILLA), MARSHMALLOW (SUGAR ,CORN SYRUP , MODIFIED STARCH, GELATIN, SODIUM HEXAMETAPHOSPHATE, ARTIFICIAL FLAVOR , NATURAL FLAVOR , ARTIFICIAL COLO (BLUE 1)), GRAHAM CRACKER (CORN STARCH, BROWN SUGAR , CORN FLOUR, PALM FAT , SOY FLOUR , SOY BRAN, HONEY, MODIFIED TAPIOCA STARCH, AMMONIUM BICARBONATE, BAKING SODA, SALT, CARAMELIZED SUGAR) NATURAL FLAVOR, CANNABIS EXTRACT.

Looking for simple clean modern design , chocolate bar can be like marivel of like the Brisbury one with images on it , and gummy is a mylar bag I really like the Brisbury style , I can provide dieline etc thank you !

Target Market(s)

Young adults

Industry/Entity Type

Cannabis , Delta 8 , CBD

Requirements
Must have
• Chocolate bar is box , dielines Included with images
Nice to have
• Simple clean , elegant and modern design , like the marivel and Brisbury brands , white logo preferred

```html
<!DOCTYPE html>
<html lang="en">
<head>
<meta charset="utf-8">
<title>Tova Meadows — Strawberry Cheesecake Bar</title>
<link rel="stylesheet" href="https://fonts.googleapis.com/css2?family=Jost:wght@500&family=Archivo:wght@400&family=Playfair+Display:ital,wght@1,400&display=swap">
<style>
  :root {
    --page: #f3f3f3;
    --rose: #b87271;
    --rose-deep: #a45f5f;
    --charcoal: #2e2b2c;
    --charcoal-pattern: #3a3637;
    --ink: #1d1b1c;
    --blush: #e8c3c0;
    --mist: #e4e0df;
    --band-red: #c9283a;
    --band-magenta: #a8306a;
    --band-violet: #7a3a9c;
    --band-indigo: #3a2f8c;
  }
  * { box-sizing: border-box; margin: 0; padding: 0; }
  html, body { width: 1200px; height: 960px; overflow: hidden; background: var(--page); }

  .box-front {
    position: absolute; left: 80px; top: 220px;
    width: 1040px; height: 520px;
    background: linear-gradient(135deg, var(--rose) 0%, var(--rose-deep) 100%);
    box-shadow: 0 10px 30px rgba(0,0,0,.12);
    overflow: hidden;
  }

  .info-panel {
    position: absolute; left: 0; top: 0; width: 310px; height: 100%;
    background: var(--charcoal);
    display: flex; align-items: flex-end; justify-content: center; gap: 26px;
    padding: 0 40px 40px 0;
  }
  .info-panel__pattern {
    position: absolute; inset: 0;
    background: linear-gradient(160deg, var(--charcoal-pattern), var(--charcoal));
    opacity: .7;
  }
  .info-panel__facts {
    position: relative;
    writing-mode: vertical-rl;
    font-family: "Archivo", sans-serif;
    font-size: 21px; line-height: 1.3;
    color: var(--mist);
    text-align: left;
  }
  .warning-mark {
    position: relative; width: 52px; height: 48px; transform: rotate(90deg);
    align-self: center; margin-top: 180px;
  }

  .weight-seal {
    position: absolute; left: 220px; top: 12px; width: 180px; height: 180px;
  }
  .weight-seal__label {
    position: absolute; inset: 0;
    display: flex; align-items: center; justify-content: center;
    writing-mode: vertical-rl;
    font-family: "Archivo", sans-serif; font-size: 16px; line-height: 1.15;
    color: var(--ink); text-align: center; letter-spacing: .5px;
  }

  .brand-block { position: absolute; left: 420px; top: 190px; width: 590px; }
  .brand-block__tagline {
    font-family: "Playfair Display", serif; font-style: italic;
    font-size: 20px; color: var(--blush); margin-left: 4px;
  }
  .brand-block__title-wrap { position: relative; margin-top: 2px; }
  .brand-block__band {
    position: absolute; left: -18px; right: -10px; top: 36px; height: 18px;
    background: linear-gradient(90deg, var(--band-red), var(--band-magenta) 40%, var(--band-violet) 75%, var(--band-indigo));
  }
  .brand-block__name {
    position: relative;
    font-family: "Jost", sans-serif; font-weight: 500;
    font-size: 66px; line-height: 1.2; letter-spacing: 1px;
    color: var(--ink); text-transform: uppercase; white-space: nowrap;
  }
  .brand-block__flavor {
    font-family: "Archivo", sans-serif; font-size: 22px;
    letter-spacing: 6px; color: var(--blush); margin-left: 4px; margin-top: 4px;
    text-transform: uppercase;
  }
</style>
</head>
<body>
  <main class="box-front">
    <section class="info-panel">
      <div class="info-panel__pattern" role="img" aria-label="Subtle dark diamond lattice pattern"></div>
      <svg class="warning-mark" viewBox="0 0 52 48" role="img" aria-label="Cannabis warning triangle">
        <path d="M26 4 L48 44 L4 44 Z" fill="none" stroke="#e4e0df" stroke-width="3" stroke-linejoin="round"/>
      </svg>
      <p class="info-panel__facts">1000 MG THC Per package<br>100mg THC per serving<br>Made with Belgian Chocolate</p>
    </section>

    <div class="weight-seal">
      <svg viewBox="0 0 180 180" width="180" height="180" aria-hidden="true">
        <defs>
          <linearGradient id="seal-ring" x1="0" y1="0" x2="0" y2="1">
            <stop offset="0" stop-color="#c9283a"/>
            <stop offset=".55" stop-color="#a8306a"/>
            <stop offset="1" stop-color="#6a3a9c"/>
          </linearGradient>
        </defs>
        <polygon fill="url(#seal-ring)" points="170,90 156.7,103.3 163.9,120.6 146.5,127.8 146.6,146.6 127.8,146.5 120.6,163.9 103.3,156.7 90,170 76.7,156.7 59.4,163.9 52.2,146.5 33.4,146.6 33.5,127.8 16.1,120.6 23.3,103.3 10,90 23.3,76.7 16.1,59.4 33.5,52.2 33.4,33.4 52.2,33.5 59.4,16.1 76.7,23.3 90,10 103.3,23.3 120.6,16.1 127.8,33.5 146.6,33.4 146.5,52.2 163.9,59.4 156.7,76.7"/>
        <circle cx="90" cy="90" r="62" fill="#ececec"/>
      </svg>
      <p class="weight-seal__label">NET WEIGHT<br>50GRAMS</p>
    </div>

    <section class="brand-block">
      <p class="brand-block__tagline">Made with Quality California Cannabis Extracts</p>
      <div class="brand-block__title-wrap">
        <div class="brand-block__band"></div>
        <h1 class="brand-block__name">Tova Meadows</h1>
      </div>
      <p class="brand-block__flavor">Strawberry Cheesecake Bar</p>
    </section>
  </main>
</body>
</html>
```